International tourism and marketing agency needs 3 page glossy (digital) brochure

We need to update/design our sales brochure with updated events and vibrant images and videos. This needs to be a pdf with live links to images and videos. We are a social enterprise seeking to increase tourism in Kenya through our marketing company, catering to high net worth ($$) African-American professionals living in the USA.

Target Market(s)

Black Americans, High Net worth retired Americans

Industry/Entity Type

Tourism, Regional Marketing

Font styles to use
Sans Serif

Colors
00AB8E
00BBA5
67D7C9
C6EFE9
E9F9F6
EB3D1F
EC4F4E
F09395
F8D3D4
FCEDEE

Requirements
Must have
• Rich, bright colors, strong images that portray retreat, relaxation and KENYA
Nice to have
• A blend of smiling faces, animals from safari, beautiful beaches off the Indian Ocean,.Nice to have videos embedded in pdf for sharing digtitally.
Should not have
• boxy script. unprofessional images of partying or too many water images. Should not have a visual focus on non-Black Americans

```html
<!DOCTYPE html>
<html lang="en">
<head>
<meta charset="utf-8">
<title>What Will You Do in Kenya?</title>
<link rel="stylesheet" href="https://fonts.googleapis.com/css2?family=Saira+Condensed:wght@600;700&family=Barlow:wght@400;500&display=swap">
<style>
  :root {
    --backdrop: #282828;
    --paper: #ffffff;
    --kenya-green: #22a52b;
    --sunset-orange: #e8761b;
    --sunset-orange-light: #f0921f;
    --deep-red: #6a1407;
    --ink: #2e2e2e;
    --faint: #f3f3f3;
    --faint-deep: #ebebeb;
  }
  * { box-sizing: border-box; margin: 0; padding: 0; }
  html, body { width: 1200px; height: 1177px; overflow: hidden; background: var(--backdrop); }
  .page {
    position: absolute; left: 286px; top: 174px; width: 651px; height: 844px;
    background: var(--paper); overflow: hidden;
  }
  .page-header {
    position: absolute; left: 0; top: 0; width: 100%; height: 80px;
    background: var(--kenya-green); text-align: center;
  }
  .page-title {
    font-family: "Saira Condensed", sans-serif; font-weight: 700; color: #fff;
    font-size: 37px; line-height: 1; padding-top: 14px; letter-spacing: 0.2px;
  }
  .invite-pill {
    position: absolute; left: 87px; top: 64px; width: 480px; height: 37px;
    border-radius: 19px; border: 2px solid #fff;
    background: linear-gradient(90deg, var(--sunset-orange), var(--sunset-orange-light));
    font-family: "Saira Condensed", sans-serif; font-weight: 600; color: #fff;
    font-size: 20px; line-height: 33px; text-align: center;
  }
  .backdrop-art {
    position: absolute; left: 410px; top: 126px; width: 186px; height: 264px;
    background: linear-gradient(180deg, var(--faint), var(--faint-deep));
  }
  .activity-list {
    position: absolute; left: 44px; top: 134px; width: 540px;
    list-style: none; font-family: "Barlow", sans-serif; font-size: 11.2px;
    line-height: 14.4px; color: var(--ink);
  }
  .activity-list li { padding-left: 8px; position: relative; }
  .activity-list li::before {
    content: "•"; color: var(--sunset-orange); position: absolute; left: 0;
  }
  .gallery-banner {
    position: absolute; left: 45px; top: 408px; width: 275px; height: 48px;
    background: var(--sunset-orange); color: #fff;
    font-family: "Saira Condensed", sans-serif; font-weight: 700; font-size: 16.5px;
    line-height: 17px; padding: 7px 0 0 20px;
  }
  .gallery-banner svg { position: absolute; right: 12px; top: 8px; }
  .photo { position: absolute; }
  .photo-sunset { left: 46px; top: 460px; width: 274px; height: 149px;
    background: linear-gradient(180deg, #6d6f78, #d9a35a 55%, #3a3a38); }
  .photo-safari { left: 46px; top: 614px; width: 274px; height: 155px;
    background: linear-gradient(180deg, #9aa3ab, #c2875a 45%, #b06a3a); }
  .photo-skydive { left: 327px; top: 410px; width: 292px; height: 167px;
    background: linear-gradient(135deg, #1f6fb0, #2aa3c8 50%, #3b82d6); }
  .photo-market { left: 327px; top: 582px; width: 142px; height: 188px;
    background: linear-gradient(180deg, #8a5a3a, #b8613f 50%, #6b4a5e); }
  .photo-dining { left: 476px; top: 582px; width: 143px; height: 188px;
    background: linear-gradient(180deg, #a8b3b8, #7a6a55 50%, #d9c7a8); }
  .page-footer {
    position: absolute; left: 0; top: 786px; width: 100%; height: 58px;
    background: var(--deep-red); display: flex; align-items: center; justify-content: center; gap: 10px;
    font-family: "Saira Condensed", sans-serif; font-weight: 700; font-size: 27px; color: #fff;
  }
  .page-footer .accent { color: var(--sunset-orange-light); }
</style>
</head>
<body>
  <main class="page">
    <header class="page-header">
      <h1 class="page-title">WHAT WILL YOU DO IN KENYA?</h1>
    </header>
    <div class="invite-pill">OUR TOUR GUIDES AND TRUSTED TRAVEL PARTNERS INVITE YOU:</div>

    <div class="backdrop-art" role="img" aria-label="Faint map of Kenya with a waving United States flag"></div>

    <ul class="activity-list">
      <li>Private chauffeured vehicles with professional guides</li>
      <li>Great food and fare: International and local Swahili cuisine</li>
      <li>4-5 star hotel accommodations in Nairobi, Western Kenya (Kisumu) and Mombasa</li>
      <li>A private guided African wildlife safari in a national animal reserve park</li>
      <li>Cycling: Explore Coral Ridge on two wheels by cycling paths within the estate</li>
      <li>Morning Yoga with resort trainers</li>
      <li>Private African Tailoring</li>
      <li>Spectacular views, water sport activities and animal reserve safaris on the coast<br>at Africa's only Championship branded course and academy.</li>
      <li>Beauty/Hairdressing</li>
      <li>Classic horseback riding on beautiful nature trails within the secure estate</li>
      <li>Snorkeling, kayaking and stand-up paddleboarding. on the best coral gardens on the Swahili coast.</li>
      <li>Hiking adventures along nature trails and through wild terrain.</li>
      <li>Tennis on all-weather courts</li>
      <li>Spa/ Massage by trained professionals</li>
      <li>Skydiving over the incredible sights of Coral Ridge<br>and landing on our beautiful beach in front of the Beach Club</li>
    </ul>

    <div class="gallery-banner">CHECK OUT OUR PHOTO GALLERY<br>TO GET A SNEAK PEEK
      <svg width="32" height="32" viewBox="0 0 32 32" aria-hidden="true">
        <circle cx="16" cy="16" r="16" fill="#6a1407"/>
        <path d="M12 9 L23 16 L12 23 Z" fill="#fff"/>
      </svg>
    </div>

    <div class="photo photo-sunset" role="img" aria-label="Palm trees silhouetted against an ocean sunset"></div>
    <div class="photo photo-safari" role="img" aria-label="Lions on red savanna with an acacia tree and mountain"></div>
    <div class="photo photo-skydive" role="img" aria-label="Tandem skydivers above the turquoise coastline"></div>
    <div class="photo photo-market" role="img" aria-label="Shopper browsing colourful baskets at a craft market"></div>
    <div class="photo photo-dining" role="img" aria-label="Plated meal and drinks on an outdoor terrace"></div>

    <footer class="page-footer">
      <svg width="30" height="30" viewBox="0 0 30 30" aria-hidden="true">
        <circle cx="15" cy="15" r="15" fill="#f0921f"/>
        <path d="M11 8 L22 15 L11 22 Z" fill="#fff"/>
      </svg>
      <span>Reserve Your Dream Retreat <span class="accent">Today!</span></span>
    </footer>
  </main>
</body>
</html>
```